Name card design for Southeast Asian Crowdfunding Startup

We need a double paged design for our company name cards.

We are a Singapore based crowd funding startup looking to operate regionally in Southeast Asia. Our service will be to match-make borrowers and lenders for loans, equity, property etc.

We have a logo already designed and hope for that to be used in the name card.

Industry/Entity Type

It Company

```html
<!DOCTYPE html>
<html lang="en">
<head>
<meta charset="utf-8">
<title>Kelong Capital – Name Card</title>
<link rel="stylesheet" href="https://fonts.googleapis.com/css2?family=Lato:wght@400;700;900&display=swap">
<style>
  :root {
    --canvas: #e9e9ea;
    --card: #f4f2f3;
    --ink: #151515;
    --magenta: #c9226f;
    --blue: #1593d8;
    --orange: #f5901e;
    --shadow: rgba(0, 0, 0, 0.18);
  }
  * { box-sizing: border-box; margin: 0; padding: 0; }
  html, body {
    width: 1200px;
    height: 1000px;
    overflow: hidden;
    background: var(--canvas);
    font-family: "Lato", Arial, sans-serif;
    color: var(--ink);
  }
  .card {
    position: absolute;
    left: 200px;
    width: 800px;
    height: 457px;
    background: var(--card);
    box-shadow: 0 6px 18px var(--shadow);
    overflow: hidden;
  }
  .card--front { top: 28px; }
  .card--back { top: 515px; }

  .edge-band {
    position: absolute;
    left: 0; right: 0; bottom: 0;
    height: 16px;
    display: flex;
  }
  .edge-band span { flex: 1; }
  .edge-band .band-magenta { background: var(--magenta); }
  .edge-band .band-blue { background: var(--blue); }
  .edge-band .band-orange { background: var(--orange); }

  .brand {
    position: absolute;
    display: flex;
    align-items: center;
    gap: 22px;
  }
  .brand__dot {
    width: 56px;
    height: 56px;
    border-radius: 50%;
    background: var(--orange);
    flex: none;
  }
  .brand__name {
    font-weight: 400;
    line-height: 1;
    white-space: nowrap;
    color: var(--ink);
  }
  .card--front .brand { left: 190px; top: 180px; }
  .card--front .brand__name { font-size: 52px; }

  .card--back .brand { left: 60px; top: 186px; gap: 16px; }
  .card--back .brand__dot { width: 40px; height: 40px; }
  .card--back .brand__name { font-size: 32px; }

  .contact {
    position: absolute;
    left: 440px;
    top: 60px;
  }
  .contact__name {
    font-weight: 900;
    font-size: 21px;
    letter-spacing: 0.5px;
  }
  .contact__title {
    font-size: 16px;
    margin-top: 4px;
  }
  .contact__list {
    list-style: none;
    margin-top: 52px;
  }
  .contact__list li {
    display: flex;
    align-items: baseline;
    font-size: 18px;
    line-height: 30px;
  }
  .contact__key {
    width: 32px;
    font-weight: 900;
    font-size: 17px;
  }
  .key-magenta { color: var(--magenta); }
  .key-blue { color: var(--blue); }
  .key-orange { color: var(--orange); }
  .contact__web {
    margin-top: 52px;
    font-weight: 900;
    font-size: 18px;
  }
</style>
</head>
<body>

  <section class="card card--front" aria-label="Card front">
    <div class="brand">
      <span class="brand__dot"></span>
      <p class="brand__name">Kelong Capital</p>
    </div>
    <div class="edge-band">
      <span class="band-magenta"></span><span class="band-blue"></span><span class="band-orange"></span>
    </div>
  </section>

  <section class="card card--back" aria-label="Card back">
    <div class="brand">
      <span class="brand__dot"></span>
      <p class="brand__name">Kelong Capital</p>
    </div>
    <div class="contact">
      <p class="contact__name">YOUR NAME</p>
      <p class="contact__title">Title</p>
      <ul class="contact__list">
        <li><span class="contact__key key-magenta">T</span>(210) 318 402 557</li>
        <li><span class="contact__key key-blue">M</span>(362) 945 170 284</li>
        <li><span class="contact__key key-orange">F</span>(518) 206 739 641</li>
        <li><span class="contact__key key-magenta">E</span>yourname@kelongcap.com</li>
      </ul>
      <p class="contact__web">www.kelongcapital.com</p>
    </div>
    <div class="edge-band">
      <span class="band-magenta"></span><span class="band-blue"></span><span class="band-orange"></span>
    </div>
  </section>

</body>
</html>
```